New letter head for Air Conditioning business

We need a new professional letter head design to suit our new re-branded air conditioning business. Our new logo is attached

```html
<!DOCTYPE html>
<html lang="en">
<head>
<meta charset="UTF-8">
<title>Norvale Air Conditioning &amp; Refrigeration — Letterhead</title>
<link href="https://fonts.googleapis.com/css2?family=Arimo:wght@700&display=swap" rel="stylesheet">
<style>
  :root {
    --band-dark: #465b48;
    --band-light: #719672;
    --brand-green: #1aff1a;
    --ink: #0a0a0a;
    --paper: #ffffff;
  }
  html, body {
    margin: 0;
    padding: 0;
    overflow: hidden;
    background: var(--paper);
  }
  .letterhead {
    position: relative;
    width: 848px;
    height: 1200px;
    overflow: hidden;
    background: var(--paper);
    font-family: "Arimo", Arial, sans-serif;
  }
  .band {
    position: absolute;
    left: 0;
    width: 848px;
  }
  .band--top { top: 0; height: 115px; }
  .band--bottom { bottom: 0; height: 71px; }
  .band .tone-dark { fill: var(--band-dark); }
  .band .tone-light { fill: var(--band-light); }

  .brand {
    position: absolute;
    left: 55px;
    top: 52px;
    display: flex;
    align-items: center;
    gap: 26px;
  }
  .brand__mark {
    width: 100px;
    height: 100px;
    border-radius: 50%;
    background: var(--band-dark);
    flex: none;
  }
  .brand__text {
    display: flex;
    flex-direction: column;
  }
  .brand__name {
    font-size: 40px;
    font-weight: 700;
    color: var(--ink);
    letter-spacing: 9px;
    line-height: 1;
    margin: 0;
  }
  .brand__tagline {
    margin: 12px 0 0;
    font-size: 10.5px;
    font-weight: 700;
    color: var(--brand-green);
    letter-spacing: 3.6px;
    line-height: 1;
    white-space: nowrap;
  }
</style>
</head>
<body>
  <main class="letterhead">
    <svg class="band band--top" viewBox="0 0 848 115" aria-hidden="true">
      <polygon class="tone-dark" points="0,0 689,0 637,41 0,41"/>
      <polygon class="tone-light" points="689,0 848,0 848,114 505,114 457,41 637,41"/>
    </svg>

    <header class="brand">
      <div class="brand__mark" aria-hidden="true"></div>
      <div class="brand__text">
        <h1 class="brand__name">NORVALE</h1>
        <p class="brand__tagline">AIR CONDITIONING &amp; REFRIGERATION</p>
      </div>
    </header>

    <svg class="band band--bottom" viewBox="0 1129 848 71" aria-hidden="true">
      <polygon class="tone-dark" points="262,1164 848,1164 848,1200 286,1200"/>
      <polygon class="tone-light" points="0,1129 235,1129 286,1200 0,1200"/>
    </svg>
  </main>
</body>
</html>
```